Willow Table Kitchen February contest

The website slider is 990 X 225 pixels to fit in with this website www.willowtablekitchen.com.au
We would love a fun, lively, food-oriented slider created for Willow Table Kitchen website. Willow Table Kitchen is a central place where people who love food, cooking for their family and friends, and sharing recipes can hang out. We'd like the sliders to be simple, bright and to entice people to click on the link.
The banner ad needs to feature the Kestral mixer, and to use a colour scheme that also works with the existing website. There's a blog with more information on the Kestral mixer here http://willowtablekitchen.com.au/uncategorized/upload-a-recipe-in-february-to-be-in-the-running-to-win-a-kestral-mixer/
A slider in December was used to promote a similar competition which I will upload as inspiration, along with the image of the Kestral mixer to use.
Main text: Add your best recipe by February 28 to win!
Smaller text: Best recipe as chosen by Willow Table Kitchen editors will win a Kestral mixer worth $699.
Target Market(s)
Food lovers - home cooks and food bloggers. Mainly women, 30+
Industry/Entity Type
Chef
Look and feel
Each slider illustrates characteristics of the customer's brand and the style your logo design should communicate.

```html
<!DOCTYPE html>
<html lang="en">
<head>
<meta charset="utf-8">
<title>Willow Table Kitchen</title>
<link href="https://fonts.googleapis.com/css2?family=Arimo:wght@400;700&family=Kaushan+Script&family=PT+Sans+Narrow:wght@400;700&display=swap" rel="stylesheet">
<style>
  :root {
    --stage: #f4f4f4;
    --paper: #efe3cf;
    --paper-light: #f8f1e7;
    --white: #ffffff;
    --brown: #4a2a1a;
    --brown-soft: #6b4a36;
    --orange: #e0531c;
    --orange-light: #f2a66e;
    --text: #333333;
    --star: #c9565a;
  }
  * { box-sizing: border-box; margin: 0; padding: 0; }
  html, body { width: 1200px; height: 1000px; overflow: hidden; background: var(--stage); }
  body { font-family: "Arimo", Arial, sans-serif; color: var(--text); }

  .page {
    position: absolute; left: 0; top: 166px;
    width: 962px; height: 535px;
    transform: scale(1.2474); transform-origin: 0 0;
    background: var(--paper); overflow: hidden;
  }
  .abs { position: absolute; }

  .brand-badge {
    left: 62px; top: -15px; width: 150px; height: 150px; border-radius: 50%;
    background: var(--white); border: 3px solid var(--brown);
    display: flex; align-items: center; justify-content: center; text-align: center;
    z-index: 3;
  }
  .brand-name { font-weight: 700; font-size: 19px; line-height: 1.15; color: var(--brown); width: 110px; margin-top: 14px; }

  .join-cta { left: 342px; top: 30px; font-family: "Kaushan Script", cursive; font-size: 22px; color: var(--brown); }
  .join-arrow { left: 635px; top: 30px; }

  .account-tab {
    left: 787px; top: 0; width: 100px; height: 22px; background: var(--white);
    border-radius: 0 0 4px 4px; font-size: 10.5px; display: flex; gap: 10px;
    justify-content: center; align-items: center; color: var(--orange);
  }

  .nav-primary {
    left: 216px; top: 83px; width: 254px; height: 34px; background: var(--white);
    display: flex; align-items: center; gap: 14px; padding-left: 18px;
    font-size: 10.5px; font-weight: 700; color: var(--brown);
  }
  .nav-primary span { display: flex; align-items: center; gap: 4px; }
  .nav-secondary {
    left: 470px; top: 83px; width: 417px; height: 34px; background: var(--orange);
    border-radius: 0 4px 0 0; display: flex; align-items: center; gap: 7px; padding-left: 27px;
    font-size: 10.5px; font-weight: 700; color: var(--white);
  }
  .nav-secondary i { font-style: normal; font-size: 8px; }

  .hero { left: 62px; top: 120px; width: 825px; height: 187px; overflow: hidden;
    background: linear-gradient(90deg, #d9c3a3, #ecdcc2); }
  .hero-photo { left: 0; top: 0; width: 535px; height: 187px;
    background: linear-gradient(100deg, #a56a4a 0%, #6b3b23 30%, #c9b9b0 55%, #4bb2cf 75%, #e7dccb 100%); }
  .hero-ribbon { left: 546px; top: 28px; background: var(--orange); color: var(--white);
    font-family: "PT Sans Narrow", sans-serif; font-size: 20px; padding: 0 18px 0 6px; height: 24px; line-height: 24px;
    clip-path: polygon(0 0, 100% 0, 92% 100%, 0 100%); }
  .hero-best { left: 580px; top: 50px; color: var(--brown); font-family: "PT Sans Narrow", sans-serif; font-weight: 700; font-size: 50px; line-height: 50px; }
  .hero-recipe { left: 680px; top: 40px; color: var(--brown); font-family: "Kaushan Script", cursive; font-size: 48px; line-height: 58px; }
  .hero-date { left: 660px; top: 95px; color: var(--orange); font-family: "PT Sans Narrow", sans-serif; font-weight: 700; font-size: 15px; letter-spacing: 1px; }
  .hero-win { left: 578px; top: 108px; color: var(--brown); font-family: "PT Sans Narrow", sans-serif; font-size: 44px; line-height: 44px; }
  .hero-win b { font-weight: 700; }
  .hero-note { left: 585px; top: 152px; width: 180px; text-align: center; color: var(--brown); font-family: "PT Sans Narrow", sans-serif; font-weight: 700; font-size: 9.5px; line-height: 11px; }

  .content { left: 62px; top: 307px; width: 825px; height: 228px; background: var(--white); }
  .section-title { display: flex; align-items: center; gap: 8px; font-size: 16.5px; color: var(--text); }
  .featured-title { left: 10px; top: 22px; }

  .recipe-card { top: 57px; width: 167px; height: 171px; background: var(--paper-light); }
  .recipe-photo { height: 113px; }
  .recipe-name { font-size: 11.5px; margin: 11px 9px 0; color: var(--text); }
  .recipe-author { font-size: 9.5px; margin: 7px 9px 0; color: var(--orange); }

  .search-box { left: 566px; top: 13px; width: 247px; height: 30px; background: var(--paper-light);
    border: 1px solid #efd9c2; border-radius: 4px; display: flex; align-items: center; justify-content: space-between;
    padding: 0 10px; font-style: italic; font-size: 11px; color: var(--text); }
  .search-scope { left: 706px; top: 48px; font-size: 10.5px; color: #555; display: flex; gap: 6px; align-items: center; }
  .radio { width: 10px; height: 10px; border-radius: 50%; border: 1px solid #888; background: var(--white); display: inline-block; vertical-align: middle; margin-left: 3px; }
  .radio.on { background: radial-gradient(circle, #2a6fb8 35%, #fff 40%); }

  .rated-title { left: 566px; top: 82px; }
  .rated-photo { left: 566px; width: 112px; }
  .rated-index { left: 566px; top: 143px; width: 17px; height: 20px; background: var(--white); font-size: 9px; color: var(--orange); display: flex; align-items: center; justify-content: center; }
  .rated-name { left: 686px; font-size: 10.5px; line-height: 16px; width: 135px; color: var(--text); }
  .rated-author { left: 686px; top: 163px; font-size: 10.5px; color: var(--orange); }
  .rated-stars { left: 686px; top: 175px; }
</style>
</head>
<body>
<div class="page">

  <div class="abs brand-badge"><div class="brand-name">Willow Table Kitchen</div></div>

  <div class="abs join-cta">Join the community now!</div>
  <svg class="abs join-arrow" width="40" height="22" viewBox="0 0 40 22" aria-hidden="true">
    <path d="M2 18 Q20 20 34 6" fill="none" stroke="#e0531c" stroke-width="1.6"/>
    <path d="M27 5 L35 5 L33 13" fill="none" stroke="#e0531c" stroke-width="1.6"/>
  </svg>

  <div class="abs account-tab"><span>Register</span><span>Login</span></div>

  <nav class="abs nav-primary">
    <span><svg width="16" height="12" viewBox="0 0 16 12" aria-hidden="true"><path d="M1 4 H15 Q14 11 8 11 Q2 11 1 4Z" fill="#e0531c"/><path d="M9 4 L14 0" stroke="#4a2a1a" stroke-width="1.4"/></svg>Recipes</span>
    <span><svg width="14" height="13" viewBox="0 0 14 13" aria-hidden="true"><circle cx="4" cy="5" r="3.5" fill="#e0531c"/><circle cx="10" cy="5" r="3.5" fill="#e0531c"/><circle cx="7" cy="3.5" r="3.5" fill="#e0531c"/><rect x="3" y="7" width="8" height="5" fill="#e0531c"/></svg>Chefs</span>
    <span><svg width="16" height="13" viewBox="0 0 16 13" aria-hidden="true"><circle cx="4" cy="3" r="2.6" fill="#e0531c"/><circle cx="12" cy="3" r="2.6" fill="#e0531c"/><circle cx="8" cy="5" r="2.8" fill="#e0531c"/><rect x="1" y="7" width="14" height="5" rx="2.5" fill="#e0531c"/></svg>Mentors</span>
  </nav>
  <nav class="abs nav-secondary">
    <span>Upload your recipe</span><i>●</i><span>Prizes</span><i>●</i><span>About</span><i>●</i><span>FAQs</span><i>●</i><span>Contact</span><i>●</i><span>Blog</span>
  </nav>

  <section class="abs hero">
    <div class="abs hero-photo" role="img" aria-label="Chocolate cheesecake and berry tarts beside a turquoise Kestral stand mixer"></div>
    <div class="abs hero-ribbon">ADD YOUR</div>
    <div class="abs hero-best">BEST</div>
    <div class="abs hero-recipe">Recipe</div>
    <div class="abs hero-date">BY FEBRUARY 28</div>
    <div class="abs hero-win">TO <b>WIN!!!</b></div>
    <div class="abs hero-note">Best recipe as chosen by Willow Table Kitchen editors will win a Kestral mixer worth $699.</div>
  </section>

  <section class="abs content">
    <h2 class="abs section-title featured-title">
      <svg width="16" height="12" viewBox="0 0 16 12" aria-hidden="true"><path d="M1 4 H15 Q14 11 8 11 Q2 11 1 4Z" fill="#e0531c"/><path d="M9 4 L14 0" stroke="#4a2a1a" stroke-width="1.4"/></svg>
      <span style="font-weight:400">Featured Recipes</span>
    </h2>

    <article class="abs recipe-card" style="left:8px">
      <div class="recipe-photo" role="img" aria-label="Plate of open cacciatore lasagne" style="background:radial-gradient(circle at 50% 55%, #c8733a 0%, #e9d8c4 45%, #f3efe9 65%, #2c3a2a 100%)"></div>
      <div class="recipe-name">Open Cacciatore Lasagne</div>
      <div class="recipe-author">By Marion Ashcroft</div>
    </article>
    <article class="abs recipe-card" style="left:191px">
      <div class="recipe-photo" role="img" aria-label="Bowl of spaghetti bolognaise topped with cheese" style="background:radial-gradient(circle at 50% 45%, #7a3c20 0%, #d7b070 35%, #f2eee6 60%, #b35a4a 100%)"></div>
      <div class="recipe-name">Spaghetti Bolognaise</div>
      <div class="recipe-author">By Helen Pryce</div>
    </article>
    <article class="abs recipe-card" style="left:375px">
      <div class="recipe-photo" role="img" aria-label="Bowl of vegetable stock with potatoes and greens" style="background:radial-gradient(circle at 45% 55%, #b08a2e 0%, #7b7a3a 35%, #e8e6e0 62%, #b9b3a8 100%)"></div>
      <div class="recipe-name">Clean Eating Vegetable Stock</div>
      <div class="recipe-author">By Dana Whitlock</div>
    </article>

    <div class="abs search-box">
      <span>search</span>
      <svg width="18" height="18" viewBox="0 0 18 18" aria-hidden="true"><circle cx="7.5" cy="7.5" r="5.5" fill="none" stroke="#f2a66e" stroke-width="2.2"/><path d="M11.5 11.5 L16 16" stroke="#f2a66e" stroke-width="2.6" stroke-linecap="round"/></svg>
    </div>
    <div class="abs search-scope"><span>Recipes<i class="radio on"></i></span><span>Chefs<i class="radio"></i></span></div>

    <h2 class="abs section-title rated-title">
      <svg width="16" height="12" viewBox="0 0 16 12" aria-hidden="true"><path d="M1 4 H15 Q14 11 8 11 Q2 11 1 4Z" fill="#e0531c"/><path d="M9 4 L14 0" stroke="#4a2a1a" stroke-width="1.4"/></svg>
      <span style="font-weight:400">Highest Rated Recipes</span>
    </h2>

    <div class="abs rated-photo" role="img" aria-label="White chocolate parfait with lemon curd" style="top:117px;height:76px;background:linear-gradient(120deg, #d8882e 0%, #f1ead8 45%, #e5d3a8 70%, #a95c26 100%)"></div>
    <div class="abs rated-index">1</div>
    <div class="abs rated-name" style="top:117px">White Chocolate Parfait W/ Lemon Curd and Short ..</div>
    <div class="abs rated-author">By Graham Lowry</div>
    <svg class="abs rated-stars" width="68" height="14" viewBox="0 0 68 14" aria-label="Five stars">
      <g fill="#c9565a">
        <path id="star" d="M7 0.5 L8.9 4.8 L13.5 5.2 L10 8.3 L11 12.9 L7 10.5 L3 12.9 L4 8.3 L0.5 5.2 L5.1 4.8Z"/>
        <use href="#star" x="13.5"/><use href="#star" x="27"/><use href="#star" x="40.5"/><use href="#star" x="54"/>
      </g>
    </svg>

    <div class="abs rated-photo" role="img" aria-label="Tray of hot cross buns" style="top:208px;height:30px;background:linear-gradient(180deg, #3a3a3a, #8a6a4a)"></div>
    <div class="abs rated-name" style="top:208px">Hot Cross Buns</div>
  </section>

</div>
</body>
</html>
```